Finally a Vodka produced for women ! (Label Design)

We are a small distillery based in Melbourne, Australia and we need a Vodka label design solution that will appeal to women aged 30-50 years and radiate luxury. Full Details are in a design brief attached. We thank you in advance.

Target Market(s)

Affluent females 30-50 years.

Industry/Entity Type

Spirits/Alcohol

Requirements
Must have
• Be clear this is a luxury Vodka.
Nice to have
• Elegance.

```html
<!DOCTYPE html>
<html lang="en">
<head>
<meta charset="utf-8">
<title>Blush Opal Vodka – Label System</title>
<link rel="stylesheet" href="https://fonts.googleapis.com/css2?family=Jost:wght@600;700&family=Montserrat:wght@700&family=Yellowtail&display=swap">
<style>
  :root{
    --purple:#a44fa0;
    --salmon:#d97c7c;
    --blush:#f6cdca;
    --band-salmon:#d9807b;
    --ink:#000;
    --glass-top:#dcb4cf;
    --glass-bottom:#c27fb3;
  }
  *{margin:0;padding:0;box-sizing:border-box}
  html,body{width:1200px;height:675px;overflow:hidden}
  body{
    position:relative;
    background:linear-gradient(180deg,var(--purple) 0%,#c0689a 35%,var(--salmon) 58%,#c0679a 74%,var(--purple) 84%,var(--purple) 100%);
    font-family:"Montserrat",sans-serif;
  }

  /* neck bands */
  .band{position:absolute;left:127px;width:484px;height:49px}
  .band svg{position:absolute;inset:0}
  .band-row{position:absolute;inset:0;display:flex;align-items:center;justify-content:space-between;padding:0 24px 0 16px}
  .band--salmon{top:56px}
  .band--black{top:130px}
  .pair{display:flex;align-items:baseline;gap:4px}
  .word-vodka{font-family:"Jost",sans-serif;font-weight:700;letter-spacing:-0.5px;line-height:1}
  .script{font-family:"Yellowtail",cursive;line-height:1}
  .band--salmon .word-vodka{font-size:19px;color:var(--ink)}
  .band--salmon .script{font-size:19px;color:var(--ink)}
  .band-maker{font-weight:700;font-size:7.5px;letter-spacing:3px;text-align:center;line-height:1.3;color:var(--ink)}
  .band--black .band-row{padding:0 20px 0 20px}
  .band--black .script{font-size:22px;color:var(--blush)}
  .band--black .word-vodka{font-size:33px;color:var(--blush)}

  /* front label */
  .label{position:absolute;left:160px;top:236px;width:420px;height:400px}
  .label-frame{position:absolute;left:53px;top:7px}
  .label-script{position:absolute;left:0;right:0;top:24px;text-align:center;font-family:"Yellowtail",cursive;font-size:48px;color:var(--blush);line-height:1}
  .label-filtered{position:absolute;left:0;right:0;top:74px;text-align:center;font-weight:700;font-size:13px;letter-spacing:2.5px;color:var(--ink)}
  .label-vodka{position:absolute;left:0;right:0;top:90px;text-align:center;font-family:"Jost",sans-serif;font-weight:600;font-size:100px;letter-spacing:-4px;color:var(--blush);line-height:1}
  .label-premium{position:absolute;left:0;right:0;top:180px;text-align:center;font-weight:700;font-size:18px;letter-spacing:20px;padding-left:20px;color:var(--ink)}
  .label-origin{position:absolute;left:-10px;right:-10px;top:226px;text-align:center;font-weight:700;font-size:13.5px;letter-spacing:2.2px;color:var(--ink)}
  .label-maker{position:absolute;left:0;right:0;top:248px;text-align:center;font-weight:700;font-size:17px;letter-spacing:7px;padding-left:7px;line-height:1.3;color:var(--ink)}
  .label-strength{position:absolute;left:0;right:0;top:360px;text-align:center;font-weight:700;font-size:16px;letter-spacing:2px;line-height:1.15;color:var(--blush)}

  /* bottle mock-up area */
  .bottle-visual{
    position:absolute;left:746px;top:50px;width:308px;height:575px;
    background:linear-gradient(180deg,var(--glass-top),var(--glass-bottom));
    border-radius:6px;
  }
</style>
</head>
<body>

  <div class="band band--salmon">
    <svg width="484" height="49" viewBox="0 0 484 49" aria-hidden="true">
      <polygon points="14,0 470,0 484,24.5 470,49 14,49 0,24.5" fill="var(--band-salmon)"/>
      <polygon points="18,5 466,5 478,24.5 466,44 18,44 6,24.5" fill="none" stroke="var(--ink)" stroke-width="1.4"/>
    </svg>
    <div class="band-row">
      <div class="pair"><span class="word-vodka">VODKA</span><span class="script">Blush Opal</span></div>
      <div class="band-maker">KESTREL<br>LANE<br>DISTILLERY</div>
      <div class="pair"><span class="word-vodka">VODKA</span><span class="script">Blush Opal</span></div>
    </div>
  </div>

  <div class="band band--black">
    <svg width="484" height="49" viewBox="0 0 484 49" aria-hidden="true">
      <polygon points="14,0 470,0 484,24.5 470,49 14,49 0,24.5" fill="var(--ink)"/>
      <polygon points="18,5 466,5 478,24.5 466,44 18,44 6,24.5" fill="none" stroke="var(--blush)" stroke-width="1.4"/>
    </svg>
    <div class="band-row">
      <span class="script">Blush Opal</span>
      <span class="word-vodka">VODKA</span>
      <span class="script">Blush Opal</span>
    </div>
  </div>

  <div class="label">
    <svg class="label-frame" width="320" height="212" viewBox="0 0 320 212" aria-hidden="true">
      <path d="M45,212 C10,170 0,140 12,110 C25,80 40,70 70,52 L140,10 Q160,0 180,10 L250,52 C280,70 295,80 308,110 C320,140 310,170 275,212"
            fill="none" stroke="var(--ink)" stroke-width="18"/>
    </svg>
    <div class="label-script">Blush Opal</div>
    <div class="label-filtered">FILTERED</div>
    <div class="label-vodka">VODKA</div>
    <div class="label-premium">PREMIUM</div>
    <div class="label-origin">HANDCRAFTED IN MELBOURNE, AUSTRALIA BY</div>
    <div class="label-maker">KESTREL<br>LANE<br>DISTILLERY</div>
    <div class="label-strength">40% ALC/VOL<br>700ML</div>
  </div>

  <div class="bottle-visual" role="img" aria-label="Illustration of the faceted pink glass vodka bottle with black cap, neck tag and front label applied"></div>

</body>
</html>
```